Disability Service Provider Expo Banner that will stand out amongst the competition

We would like to have a two banners designed to be able to display at expos that outline the services that we provide as a company. We are a disability service provider who aims to provider services to increase the independence of those living with a disability. We would like the banners to follow consistent themes/designs from other marketing material that we have (see brief for designs). One of the banners will be for the allied health services we provide (exercise physiology and occupational therapy) and the other banner will be promoting the our support worker, programs, and short-term accommodation. Our main colour schemes for therapy are black, yellow, and white. For our other services we utilise yellow, blue, and magenta as part of our colour pallet. Please utilise the information from the flyers, colours, and logos all located in the design brief. The style of banner can be seen in the images upload in the brief.

Target Market(s)

Parents and carers of those who livce with a disability, and seeking their business over our competitors

Industry/Entity Type

Disability Service and Health Provider

Colors

Designer to choose colors to be used in the design.

Requirements
Must have
• Eye catching, limited text
Nice to have
• Split services across a few banners
Should not have
• Lots of words

```html
<!DOCTYPE html>
<html lang="en">
<head>
<meta charset="utf-8">
<title>Larkfield Exercise Physiology Banner</title>
<link rel="stylesheet" href="https://fonts.googleapis.com/css2?family=Montserrat:ital,wght@0,400;0,500;0,700;0,800;1,800;1,900&display=swap">
<style>
  :root {
    --ink: #000000;
    --paper: #ffffff;
    --sun: #f2d833;
    --sun-edge: #d9bf1f;
    --chip: #c9c9c9;
    --chip-edge: #a9a9a9;
    --photo-light: #b9c4cc;
    --photo-blue: #4f98c4;
    --photo-floor: #5f6468;
  }
  * { margin: 0; padding: 0; box-sizing: border-box; }
  html, body { width: 1200px; height: 2227px; overflow: hidden; background: var(--ink); }
  .banner {
    position: relative; width: 1200px; height: 2227px;
    background: var(--ink); font-family: "Montserrat", sans-serif; color: var(--paper);
  }
  .brand {
    position: absolute; top: 107px; left: 0; width: 100%;
    display: flex; flex-direction: column; align-items: center;
  }
  .brand-dot { width: 120px; height: 120px; border-radius: 50%; background: var(--sun); margin-left: 230px; }
  .brand-name { margin-top: 28px; font-size: 118px; font-weight: 800; letter-spacing: 2px; line-height: 1; color: var(--paper); }
  .headline {
    position: absolute; top: 460px; left: 0; width: 100%; text-align: center;
    color: var(--sun); font-weight: 800; font-size: 124px; line-height: 112px; letter-spacing: -1px;
  }
  .tagline {
    position: absolute; top: 702px; left: 0; width: 100%; text-align: center;
    font-size: 42px; line-height: 54px; font-weight: 400;
  }
  .tagline strong { font-weight: 700; }
  .photo {
    position: absolute; top: 880px; left: 0; width: 1200px; height: 860px;
    background:
      linear-gradient(to bottom, var(--ink) 0%, rgba(0,0,0,0) 14%, rgba(0,0,0,0) 70%, var(--ink) 100%),
      radial-gradient(ellipse at 45% 35%, var(--photo-blue) 0%, rgba(79,152,196,0.4) 35%, rgba(0,0,0,0) 60%),
      linear-gradient(to bottom, var(--photo-light) 0%, #8e9aa2 50%, var(--photo-floor) 80%);
  }
  .pillars {
    position: absolute; top: 1700px; left: 0; width: 100%; height: 78px;
  }
  .pill {
    position: absolute; top: 0; height: 78px; border-radius: 10px;
    display: flex; align-items: center; justify-content: center;
    font-weight: 900; font-style: italic; font-size: 44px; color: #111;
    background: var(--chip); border: 4px solid var(--chip-edge);
    box-shadow: 0 14px 10px -6px rgba(0,0,0,0.7);
  }
  .pill-fit { left: 75px; width: 316px; }
  .pill-healthy { left: 411px; width: 390px; background: var(--sun); border-color: var(--sun-edge); }
  .pill-fun { left: 818px; width: 317px; }
  .contact-wave { position: absolute; left: 0; top: 0; width: 1200px; height: 2227px; }
  .contact {
    position: absolute; top: 2000px; left: 0; width: 100%; text-align: center; color: var(--ink);
  }
  .contact-phone {
    display: flex; align-items: center; justify-content: center; gap: 18px;
    font-size: 66px; line-height: 78px; font-weight: 500;
  }
  .contact-phone strong { font-weight: 800; }
  .contact-web { margin-top: 6px; font-size: 62px; line-height: 72px; font-weight: 500; }
  .contact-web strong { font-weight: 800; }
</style>
</head>
<body>
<main class="banner">
  <header class="brand">
    <div class="brand-dot"></div>
    <div class="brand-name">LARKFIELD</div>
  </header>

  <h1 class="headline">EXERCISE<br>PHYSIOLOGY</h1>

  <p class="tagline">Improve your <strong>health, quality of life,<br>&amp; independence</strong> with the help of<br>our Excersise Physiologist!</p>

  <div class="photo" role="img" aria-label="Photo: a woman with a prosthetic leg doing a crunch on a gym mat while an exercise physiologist kneels beside her, blue graffiti wall behind"></div>

  <div class="pillars">
    <div class="pill pill-fit">GET FIT</div>
    <div class="pill pill-healthy">BE HEALTHY</div>
    <div class="pill pill-fun">HAVE FUN</div>
  </div>

  <svg class="contact-wave" viewBox="0 0 1200 2227" aria-hidden="true">
    <path fill="#f2d833" d="M0 1990 C30 2000 55 2012 75 2025 C110 1930 210 1868 330 1868 C450 1868 580 1900 648 1960 C690 1910 760 1880 840 1880 C960 1880 1080 1940 1122 2040 C1150 2025 1175 2015 1200 2010 L1200 2227 L0 2227 Z"/>
  </svg>

  <section class="contact">
    <div class="contact-phone">
      <svg width="72" height="72" viewBox="0 0 72 72" aria-hidden="true">
        <circle cx="36" cy="36" r="36" fill="#000"/>
        <path fill="#f2d833" d="M26 18c2 0 3 1 4 3l3 7c1 2 0 3-1 4l-3 2c2 5 6 9 11 11l2-3c1-1 2-2 4-1l7 3c2 1 3 2 3 4 0 5-4 9-9 9-15 0-28-13-28-28 0-5 4-9 8-9z"/>
      </svg>
      <span>Call <strong>1800 555 012</strong></span>
    </div>
    <div class="contact-web">www.<strong>larkfield.com</strong>.au</div>
  </section>
</main>
</body>
</html>
```